Pelmora Tours - Astronomy in the Kimberley

Pelmora Tours requires a web page to advertise astronomy tours in the East Kimberley, Australia. It needs the following tabs - Home, Tours, Astronomy Events, Gallery, Testimonials, Contacts.

It should target tourists to the Kimberley.
We are unsure of which colours to go with at the moment but we have included our logo if it helps.

It should be mobile and tablet friendly.

Target Market(s)

Families, +40, Tourist, hobby astronomists,

Industry/Entity Type

Events

Number of Pages Required

3 page

Colors
3377b5
ffffff

Requirements
Must have
• Home, Tours, Astronomy Events, Gallery, Calendar, Testimonials, Contacts.
• 'Pelmora Tours' logo
Nice to have
• Pictures of portable amateur telescopes. Pictures of Lake Kununurra or Wyndham.
Should not have
• Pictures of extremely large professional telescopes.

```html
<!DOCTYPE html>
<html lang="en">
<head>
<meta charset="utf-8">
<title>Pelmora Tours – Astronomy in the Kimberley</title>
<link href="https://fonts.googleapis.com/css2?family=Open+Sans:wght@400;600;700&family=Tinos&display=swap" rel="stylesheet">
<style>
:root{
  --brand:#3377b5;
  --brand-dark:#1f4f8a;
  --white:#ffffff;
  --page:#f5f5f5;
  --header:#efefef;
  --ink:#333333;
  --muted:#8e8e8e;
  --line:#dcdcdc;
  --orange:#f0955f;
  --red:#ee5a67;
  --sky:#5bb6e6;
  --footer:#2e2e2e;
  --footer-bottom:#262626;
  --footer-text:#cfcfcf;
  --link:#4b8fd0;
}
*{margin:0;padding:0;box-sizing:border-box}
html,body{width:1200px;height:3046px;overflow:hidden}
body{font-family:"Open Sans",Arial,sans-serif;background:var(--page);color:var(--ink);position:relative}
.abs{position:absolute}

/* header */
.site-header{position:absolute;left:0;top:0;width:1200px;height:142px;background:var(--header);border-top:6px solid var(--brand)}
.nav{position:absolute;top:58px;font-size:13px;font-weight:700;text-transform:uppercase;color:#333;display:flex;gap:30px}
.nav a{color:inherit;text-decoration:none}
.nav .active{color:var(--brand)}
.nav-left{right:660px}
.nav-right{left:696px}
.brand{position:absolute;left:0;width:1200px;top:34px;text-align:center}
.brand-mark{width:44px;height:44px;border-radius:50%;background:var(--brand);margin:0 auto 6px}
.brand-name{font-size:20px;font-weight:600;color:var(--brand);line-height:1}

/* hero */
.hero{position:absolute;left:0;top:142px;width:1200px;height:593px;
  background:linear-gradient(180deg,#7aa6d8 0%,#b9d0e6 22%,#6b4d3d 32%,#4c7fa6 40%,#b5aea3 50%,#a49c90 80%,#7d8c5c 100%)}
.hero-arrow{position:absolute;top:270px;font-size:48px;color:var(--white);line-height:1}
.caption{position:absolute;left:101px;top:410px;width:997px;height:148px;background:rgba(255,255,255,.45);padding:22px 22px}
.caption h2{font-size:34px;font-weight:700;color:var(--brand-dark);line-height:1}
.caption p{font-size:13px;color:#fff;margin-top:10px;line-height:1.5}
.dots{position:absolute;left:467px;top:122px;display:flex;gap:4px}
.dots span{width:16px;height:16px;border-radius:50%;background:var(--white)}

/* welcome */
.welcome-title{position:absolute;left:0;width:1200px;top:826px;text-align:center;font-family:"Tinos","Times New Roman",serif;font-size:80px;letter-spacing:4px;color:#222;line-height:1}
.welcome-text{position:absolute;left:290px;width:620px;top:938px;text-align:center;font-size:14px;line-height:21px;color:var(--muted)}
.divider{position:absolute;left:97px;top:1097px;width:1003px;height:2px;background:var(--line)}
.feature{position:absolute;top:1254px;width:321px;height:173px;border:2px solid var(--line);background:var(--page);text-align:center;padding-top:70px}
.feature h3{font-size:16px;font-weight:700;color:#333;letter-spacing:.5px}
.feature p{font-size:15px;color:#a8a8a8;margin-top:14px;line-height:22px;padding:0 30px}
.feature-icon{position:absolute;top:1163px;width:130px;height:130px;border-radius:50%;background:var(--page);border:3px dotted}

/* video */
.video{position:absolute;left:0;top:1531px;width:1200px;height:507px;
  background:linear-gradient(180deg,#3c4f5f 0%,#52606b 25%,#3d4a3a 50%,#4a3a2c 80%,#3a2e26 100%)}
.video-inner{position:absolute;left:0;top:0;width:1200px;text-align:center;color:var(--white)}
.video h2{position:absolute;left:437px;width:326px;top:60px;font-size:34px;font-weight:400;border-bottom:2px solid #fff;padding-bottom:4px}
.video p{position:absolute;left:240px;width:720px;font-size:14px;font-weight:600;line-height:20px}
.play{position:absolute;left:563px;top:296px;width:74px;height:74px;border-radius:50%;border:3px solid #fff}
.watch{top:393px}

/* news */
.news-title{position:absolute;left:0;width:1200px;top:2083px;text-align:center;font-size:32px;font-weight:600;color:#333}
.news-rule{position:absolute;left:502px;width:196px;top:2138px;height:2px;background:var(--line)}
.news-rule i{position:absolute;left:56px;width:84px;height:2px;background:var(--brand)}
.news-sub{position:absolute;left:0;width:1200px;top:2150px;text-align:center;font-size:15px;font-style:italic;color:#999}
.card{position:absolute;top:2213px;width:236px;height:290px;background:var(--white);border:1px solid #e2e2e2;text-align:center}
.card .photo{height:174px}
.card h3{font-size:16px;font-weight:700;margin-top:24px;color:#333}
.card p{font-size:15px;color:#aaa;margin-top:6px}
.btn{position:absolute;top:2481px;width:158px;height:44px;border-radius:22px;background:var(--brand);color:#fff;font-size:14px;font-weight:700;text-align:center;line-height:44px}

/* footer */
.footer{position:absolute;left:0;top:2598px;width:1200px;height:388px;background:var(--footer);color:var(--footer-text)}
.footer h4{position:absolute;top:30px;font-size:24px;font-weight:400;color:#fff}
.col{position:absolute;top:92px;font-size:11px;line-height:24px}
.links li{list-style:none;color:var(--link);border-bottom:1px solid #3d3d3d;line-height:33px;width:228px}
.links li::before{content:"» ";color:#888}
.tweet{width:228px;line-height:20px;margin-bottom:14px}
.tweet b{color:var(--link);font-weight:400}
.field{width:230px;height:36px;background:#222;border:1px solid #3a3a3a;margin-bottom:9px;color:#aaa;font-size:12px;padding:8px 14px;font-family:"Tinos",serif}
.field.msg{height:82px}
.submit{width:104px;height:34px;background:var(--brand);color:#fff;font-size:11px;font-weight:700;text-align:center;line-height:34px}
.footer-bottom{position:absolute;left:0;top:2986px;width:1200px;height:60px;background:var(--footer-bottom);color:#888;font-size:12px;padding:24px 97px}
</style>
</head>
<body>

<header class="site-header">
  <nav class="nav nav-left">
    <a class="active" href="#">Home</a><a href="#">Tours</a><a href="#">Astronomy Events</a>
  </nav>
  <div class="brand">
    <div class="brand-mark"></div>
    <div class="brand-name">Pelmora Tours</div>
  </div>
  <nav class="nav nav-right">
    <a href="#">Gallery</a><a href="#">Testimonials</a><a href="#">Contacts</a>
  </nav>
</header>

<section class="hero" role="img" aria-label="Photo of an infinity pool terrace with red sun loungers overlooking Lake Kununurra and red ranges under a blue sky">
  <div class="hero-arrow" style="left:36px">&#10094;</div>
  <div class="hero-arrow" style="right:30px">&#10095;</div>
  <div class="caption">
    <h2>PROTAL :</h2>
    <p>Lorem ipsum dolor sit amet conse ctetur adipisicing elit, sed do eiusmod tempor incididunt ut labore et dolore magna aliqua. Ut enim ad minim veniam, quis nostrud exercitation ullamco laboris nisi ut aliquip ex ea commodo consequat. Duis aute irure dolor.</p>
    <div class="dots"><span></span><span></span><span></span></div>
  </div>
</section>

<h1 class="welcome-title">WELCOME!</h1>
<p class="welcome-text">Faucibus orci luctus et trices posuere cubilia Suspendisse sollicit udin velit sed leo. Ut pharetra aue nec augentum. Donec in velit vel ipsum auue. Nam elit magna Donec porta diam eu massa. Quisque diam lorem interdum vitaapibus ac scelerisque vitae pede. Donec eget tellus non erat lacinia fermentum.</p>
<div class="divider"></div>

<div class="feature" style="left:97px"><h3>HOTEL INFO</h3><p>Typi non habent claritatem insitam; est usus legentis in iis</p></div>
<div class="feature" style="left:440px"><h3>HOT TOURS</h3><p>Non habent claritatem insitam; est usus legentis in iis qui facit</p></div>
<div class="feature" style="left:781px"><h3>CONSULTING</h3><p>Aeri non habent claritatem nsitam; est usus legentis in iis</p></div>

<div class="feature-icon" style="left:193px;border-color:var(--orange)">
  <svg width="124" height="124" viewBox="0 0 124 124"><g fill="var(--orange)"><rect x="44" y="40" width="24" height="44"/><rect x="68" y="54" width="14" height="30"/></g><g fill="#fff"><rect x="48" y="45" width="6" height="6"/><rect x="58" y="45" width="6" height="6"/><rect x="48" y="56" width="6" height="6"/><rect x="58" y="56" width="6" height="6"/><rect x="48" y="67" width="6" height="6"/><rect x="58" y="67" width="6" height="6"/><rect x="72" y="60" width="6" height="6"/><rect x="72" y="70" width="6" height="6"/></g></svg>
</div>
<div class="feature-icon" style="left:535px;border-color:var(--red)">
  <svg width="124" height="124" viewBox="0 0 124 124"><path fill="var(--red)" d="M40 58 L56 56 L74 38 Q80 34 82 38 Q84 42 78 48 L66 62 L72 80 L66 84 L56 68 L46 74 L46 80 L41 82 L38 72 L30 66 L33 62 L40 64 Z"/></svg>
</div>
<div class="feature-icon" style="left:876px;border-color:var(--sky)">
  <svg width="124" height="124" viewBox="0 0 124 124"><g fill="var(--sky)"><circle cx="54" cy="64" r="8"/><path d="M38 86 Q38 72 54 72 Q70 72 70 86 Z"/><path d="M62 40 h24 a4 4 0 0 1 4 4 v12 a4 4 0 0 1 -4 4 h-14 l-8 7 v-7 h-2 a4 4 0 0 1 -4 -4 v-12 a4 4 0 0 1 4 -4z"/></g></svg>
</div>

<section class="video" role="img" aria-label="Darkened aerial photo of rugged Kimberley ranges and a river valley under cloud">
  <div class="video-inner">
    <h2>TRAVEL VIDEO</h2>
    <p style="top:148px">DUIS AUTEM VEL EUM IRIURE DOLOR IN HENDRERIT IN VULPUTATE VELIT ESSE MOLESTIE CONSEQUAT, VEL ILLUM DOLORE</p>
    <p style="top:202px">EU FEUGIAT NULLA FACILISIS AT VIM VEN</p>
    <p style="top:238px">IAM, QUIS NOSTRUD EX</p>
    <div class="play"><svg width="68" height="68" viewBox="0 0 68 68"><path d="M27 22 L47 34 L27 46 Z" fill="#2f5e8f"/></svg></div>
    <p class="watch" style="font-size:13px">WATCH THE VIDEO</p>
  </div>
</section>

<h2 class="news-title">OUR NEWS</h2>
<div class="news-rule"><i></i></div>
<p class="news-sub">Ut wisi enim ad minim veniam, quis nostrud ex</p>

<article class="card" style="left:97px"><div class="photo" role="img" aria-label="Photo of a couple relaxing on striped deck chairs by the sea" style="background:linear-gradient(180deg,#7fb2e0,#d8e6f0 55%,#b4754e)"></div><h3>LOREM IPSUM DOLO</h3><p>Quisi enim ad minim veniam,</p></article>
<article class="card" style="left:355px"><div class="photo" role="img" aria-label="Photo of a message bottle on a sunny beach" style="background:linear-gradient(180deg,#4fb3e6,#9dd6ef 50%,#c99552)"></div><h3>CLARITAS EST ETIAM</h3><p>Quisi enim ad minim veniam,</p></article>
<article class="card" style="left:611px"><div class="photo" role="img" aria-label="Photo of tropical waterfalls over a turquoise pool" style="background:linear-gradient(180deg,#5d8a3c,#e6f0f0 45%,#2fb5b8)"></div><h3>EODEM MODO</h3><p>Quisi enim ad minim veniam,</p></article>
<article class="card" style="left:867px"><div class="photo" role="img" aria-label="Photo of a beachfront resort hotel with palm trees" style="background:linear-gradient(180deg,#8cc2ea,#e8e4dc 50%,#4f7f44)"></div><h3>UT WISI ENIM</h3><p>Quisi enim ad minim veniam,</p></article>

<div class="btn" style="left:136px">MORE INFO</div>
<div class="btn" style="left:392px">MORE INFO</div>
<div class="btn" style="left:649px">MORE INFO</div>
<div class="btn" style="left:905px">MORE INFO</div>

<footer class="footer">
  <h4 style="left:97px">Contact</h4>
  <h4 style="left:355px">Quick Links</h4>
  <h4 style="left:611px">Latest Tweets</h4>
  <h4 style="left:873px">Contact Us</h4>

  <div class="col" style="left:97px">
    Korvale Holdings Pty Ltd.<br><br>
    (Melbourne Office / Head Office)<br>
    Level 4, Suite 412 / 88 Tarrow Street,<br>
    Melbourne, VIC 3000<br>
    Phone: (03) 5550 1842<br>
    (Brisbane Office)<br>
    Shop 2/417 Brindle Road,<br>
    Annerley, QLD 4103<br>
    (07) 5550 2917
  </div>

  <ul class="col links" style="left:355px;top:82px">
    <li>Lorem ipsum dolor sit</li>
    <li>Amet consectetur</li>
    <li>Praesent vel sem id</li>
    <li>Curabitur hendrerit est</li>
    <li>Aliquam eget erat nec sapien</li>
    <li>Cras id augue nunc</li>
    <li>Sed a nulla urna</li>
  </ul>

  <div class="col" style="left:611px">
    <p class="tweet"><b>@namehere</b> Justoid nonummy laoreet phasellent penatoque in antesque pellus elis eget tincidunt. Nequatdui laoreet justo a non tellus laoreumt vitae doloreet<br>1 day ago</p>
    <p class="tweet"><b>@namehere</b> Justoid nonummy laoreet phasellent penatoque in antesque pellus elis eget tincidunt. Nequatdui laoreet justo a non tellus laoreumt vitae doloreet<br>1 day ago</p>
  </div>

  <div class="col" style="left:868px;top:84px;line-height:normal">
    <div class="field">Full Name</div>
    <div class="field">Email Address</div>
    <div class="field">Subject</div>
    <div class="field msg">Message</div>
    <div class="submit" style="margin-top:10px">SUBMIT</div>
  </div>
</footer>

<div class="footer-bottom">Copyright © 2015 pelmoratours.example - All Rights Reserved</div>

</body>
</html>
```